<作成物>
■リッチメッセージ
リッチメニュー
合計2枚

【デザインの詳細】
デザインの詳細イメージをファイルに入れております。
また、別の業種の方ですが、サンプルデザインをファイルのリンク先に付けておりますのでご確認ください。
上下で一体感があるものを希望します。

〈リッチメニューの表示項目〉
左上から① ホームページ・SNS・自己紹介 ②サービス紹介 ③動画で体験
左下から④オンラインショップ ⑤お客様の声 ⑥お問い合わせ

デザイン重視でここの表示名はデザイン的に英語の方がよければ
英語でも大丈夫です。意味がわかって
ニュアンスがあっていれば文字を短くするのも
お任せします。あくまでデザイン重視です。
〈画像はこちらから〉
素材画像
https://7.kumobako.example/3081-a4f2c9e7b1d05e6f38c2a9d4e7b61f05

※こちらの作成以外に勝手に使用された場合は
著作権侵害で法的手段をとらせていただきます。
作成事例にもしようしないでください。

<サイズ>
・リッチメッセージ(1040×1040ピクセル)
・リッチメニュー(1200×810ピクセル)

<納品形式>
・ai形式(イラストレーターデータ)
・psd形式(フォトショップデータ)
・JPG
<詳細>
※添付ファイルをご確認ください。

<備考>
ブランディング効果を期待しています。
どんどん何個でも応募ください。

```html
<!DOCTYPE html>
<html lang="ja">
<head>
<meta charset="UTF-8">
<title>Lumica リッチメッセージ・リッチメニュー</title>
<link href="https://fonts.googleapis.com/css2?family=Zen+Maru+Gothic:wght@500;700&family=Noto+Serif+JP:wght@500&display=swap" rel="stylesheet">
<style>
  :root {
    --sky-light: #eef8fd;
    --sky: #bfe4f6;
    --sky-deep: #7cc3e8;
    --glow: #4aa6d8;
    --ink: #3f3f46;
    --ink-soft: #6b6b73;
    --white: #ffffff;
    --band: rgba(255,255,255,0.92);
  }
  * { margin: 0; padding: 0; box-sizing: border-box; }
  html, body { width: 774px; height: 1200px; overflow: hidden; }
  body {
    font-family: "Zen Maru Gothic", sans-serif;
    color: var(--ink);
    background: var(--white);
  }
  .canvas { position: relative; width: 774px; height: 1200px; overflow: hidden; }

  /* rich message */
  .message {
    position: absolute; left: 0; top: 0; width: 774px; height: 650px;
    background: radial-gradient(circle at 70% 20%, var(--white) 0%, var(--sky-light) 35%, var(--sky) 75%, var(--sky-deep) 100%);
  }
  .lead {
    position: absolute; top: 24px; width: 100%; text-align: center;
    font-size: 30px; font-weight: 700; color: var(--ink);
    letter-spacing: 2px;
  }
  .headline {
    position: absolute; width: 100%; text-align: center;
    color: var(--white); font-weight: 700;
    text-shadow: 0 0 6px var(--glow), 0 0 2px var(--glow), 0 0 12px var(--sky-deep);
    letter-spacing: 4px;
  }
  .headline--sound { top: 66px; font-size: 64px; }
  .headline--cross { top: 136px; font-size: 52px; }
  .headline--esthe { top: 188px; font-size: 64px; padding-left: 40px; }
  .headline__small { font-size: 32px; color: var(--ink); text-shadow: none; letter-spacing: 1px; }

  .brand-band {
    position: absolute; left: 98px; top: 306px; width: 578px; height: 52px;
    background: var(--band);
    display: flex; align-items: center; justify-content: center;
    font-family: "Noto Serif JP", serif; font-size: 30px; color: var(--ink-soft);
    letter-spacing: 6px;
  }
  .photo {
    position: absolute; left: 232px; top: 364px; width: 542px; height: 258px;
    background: linear-gradient(120deg, #f4ede8 0%, #e8d3c6 40%, #c9a997 70%, #8fb7cf 100%);
  }
  .tagline {
    position: absolute; left: 58px; top: 476px; width: 170px;
    font-size: 19px; line-height: 1.7; color: var(--ink-soft);
  }

  /* rich menu */
  .menu {
    position: absolute; left: 0; top: 650px; width: 774px; height: 550px;
    background: radial-gradient(circle at 50% 40%, var(--sky-light) 0%, var(--sky) 60%, var(--sky-deep) 100%);
  }
  .menu__item {
    position: absolute; width: 244px; height: 244px; border-radius: 50%;
    background: var(--white);
    display: flex; flex-direction: column; align-items: center; justify-content: center;
    text-align: center;
  }
  .menu__icon { width: 82px; height: 82px; margin-bottom: 10px; fill: var(--ink); }
  .menu__label { font-size: 26px; font-weight: 700; line-height: 1.2; color: var(--ink); }
  .c1 { left: 7px; } .c2 { left: 265px; } .c3 { left: 523px; }
  .r1 { top: 15px; } .r2 { top: 304px; }
</style>
</head>
<body>
<div class="canvas">
  <section class="message">
    <p class="lead">世界でたった一つの</p>
    <p class="headline headline--sound">癒しの音</p>
    <p class="headline headline--cross">×</p>
    <p class="headline headline--esthe">エステ<span class="headline__small">の融合</span></p>
    <div class="brand-band">Lumica</div>
    <div class="photo" role="img" aria-label="エステの施術を受けてくつろぐ女性の写真"></div>
    <p class="tagline">他にはない、<br>「極上の癒し」</p>
  </section>

  <nav class="menu">
    <a class="menu__item c1 r1">
      <svg class="menu__icon" viewBox="0 0 24 24"><path d="M12 3 2 12h3v8h5v-6h4v6h5v-8h3z"/></svg>
      <span class="menu__label">HP・SNS<br>自己紹介</span>
    </a>
    <a class="menu__item c2 r1">
      <svg class="menu__icon" viewBox="0 0 24 24"><path d="M11 6c.6 4 2 5.4 6 6-4 .6-5.4 2-6 6-.6-4-2-5.4-6-6 4-.6 5.4-2 6-6z"/><path d="M18 2c.3 1.7.9 2.3 2.5 2.5-1.6.3-2.2.9-2.5 2.5-.3-1.6-.9-2.2-2.5-2.5 1.6-.2 2.2-.8 2.5-2.5zM5 17c.2 1.2.7 1.7 2 2-1.3.2-1.8.7-2 2-.2-1.3-.7-1.8-2-2 1.3-.3 1.8-.8 2-2z"/></svg>
      <span class="menu__label">サービス紹介</span>
    </a>
    <a class="menu__item c3 r1">
      <svg class="menu__icon" viewBox="0 0 24 24"><circle cx="12" cy="12" r="10"/><path d="M10 8l6 4-6 4z" fill="#fff"/></svg>
      <span class="menu__label">動画で体験</span>
    </a>
    <a class="menu__item c1 r2">
      <svg class="menu__icon" viewBox="0 0 24 24"><path d="M2 3h3l3 11h10l3-8H7" fill="none" stroke="#3f3f46" stroke-width="2" stroke-linejoin="round"/><path d="M8 8h12l-2 5H9z"/><circle cx="9" cy="19" r="1.8"/><circle cx="17" cy="19" r="1.8"/></svg>
      <span class="menu__label">オンライン<br>ショップ</span>
    </a>
    <a class="menu__item c2 r2">
      <svg class="menu__icon" viewBox="0 0 24 24"><path d="M12 3c5 0 9 3.4 9 7.8S17 18.5 12 18.5c-1 0-2-.1-2.9-.4L4 21l1.4-4.3C3.9 15.3 3 13.1 3 10.8 3 6.4 7 3 12 3z" fill="none" stroke="#3f3f46" stroke-width="1.8" stroke-linejoin="round"/></svg>
      <span class="menu__label">お客様の声</span>
    </a>
    <a class="menu__item c3 r2">
      <svg class="menu__icon" viewBox="0 0 24 24"><rect x="6.5" y="2" width="11" height="20" rx="2" fill="none" stroke="#3f3f46" stroke-width="1.8"/><circle cx="12" cy="18.5" r="1"/></svg>
      <span class="menu__label">お問い合わせ</span>
    </a>
  </nav>
</div>
</body>
</html>
```